Create website design - Hire business

Build website to specification. Look and feel only or include all functionality. I have put together a google document which includes all information on requirements. I will share this with you via message once you have been assigned the job.

Coding

Coded - Design and coding required

Number of Pages Required

1 page

Requirements
Must have
• As per Google Doc
Nice to have
• As per Google Doc
Should not have
• As per Google Doc

```html
<!DOCTYPE html>
<html lang="en">
<head>
<meta charset="utf-8">
<title>Benchline Hire – Hire Tools Next Door</title>
<link href="https://fonts.googleapis.com/css2?family=Montserrat:wght@500;600;700;800&family=Open+Sans:wght@400;600;700&display=swap" rel="stylesheet">
<style>
:root{
  --blue:#1d7fd8;
  --blue-dark:#1565b3;
  --navy:#0f1f33;
  --ink:#1b2430;
  --muted:#6b7684;
  --soft:#f4f6f9;
  --line:#e3e7ec;
  --white:#ffffff;
  --dark:#17191d;
  --page:#dfe3e8;
}
*{box-sizing:border-box;margin:0;padding:0}
html,body{width:1200px;height:2352px;overflow:hidden;background:var(--page)}
body{font-family:"Open Sans",Arial,sans-serif;color:var(--ink);position:relative}
h1,h2,h3,h4,.brand,.nav a,.btn{font-family:"Montserrat",Arial,sans-serif}

/* desktop page */
.desktop{position:absolute;left:0;top:0;width:980px;height:2352px;background:var(--white);overflow:hidden}
.topbar{height:20px;background:var(--blue-dark);color:#dbe9f7;font-size:8px;display:flex;align-items:center;gap:16px;padding:0 40px}
.topbar .dot{width:6px;height:6px;border-radius:50%;background:#dbe9f7;display:inline-block;margin-right:4px}
.header{height:48px;display:flex;align-items:center;justify-content:space-between;padding:0 40px;border-bottom:1px solid var(--line)}
.brand{font-weight:800;font-size:13px;color:var(--blue);display:flex;align-items:center;gap:6px;letter-spacing:.5px}
.brand .mark{width:12px;height:12px;background:var(--blue)}
.nav{display:flex;gap:18px}
.nav a{font-size:8px;font-weight:600;color:var(--ink);text-decoration:none}
.nav a.on{color:var(--blue)}

.hero{position:relative;height:404px}
.hero-photo{position:absolute;inset:0;background:linear-gradient(100deg,#1c1f24 0%,#3a2f29 45%,#6a4d36 75%,#2a2521 100%)}
.hero-shade{position:absolute;inset:0;background:rgba(10,14,20,.45)}
.hero-copy{position:absolute;left:60px;top:170px;color:var(--white)}
.hero-copy h1{font-size:38px;font-weight:800;line-height:1.05}
.hero-copy h1 span{color:var(--blue)}
.hero-copy p{font-size:10px;margin-top:10px;color:#d7dde5}
.quote-form{position:absolute;left:690px;top:54px;width:240px;height:300px;background:var(--white);border-radius:3px;padding:22px 18px;display:flex;flex-direction:column;gap:16px}
.field{height:28px;border:1px solid var(--line);border-radius:2px;font-size:8px;color:var(--muted);display:flex;align-items:center;padding:0 10px;gap:8px}
.field i{width:7px;height:7px;border-radius:50%;background:var(--blue)}
.btn{background:var(--blue);color:var(--white);font-size:8px;font-weight:700;border:0;height:28px;border-radius:2px;display:flex;align-items:center;justify-content:center}

.features{height:168px;display:flex;justify-content:space-around;padding:34px 60px 0;border-bottom:1px solid var(--line)}
.feature{width:220px;text-align:center}
.feature svg{width:28px;height:28px}
.feature h3{font-size:10px;font-weight:700;margin:10px 0 6px}
.feature p{font-size:8px;color:var(--muted);line-height:1.5}

.services{height:380px;background:var(--soft);text-align:center;padding-top:36px}
.eyebrow{font-size:7px;letter-spacing:1.5px;color:var(--blue);font-weight:700;text-transform:uppercase}
.services h2{font-size:26px;font-weight:700;margin:6px 0 8px}
.services .lead{font-size:8px;color:var(--muted);width:520px;margin:0 auto;line-height:1.5}
.service-grid{display:grid;grid-template-columns:repeat(3,220px);gap:26px 40px;justify-content:center;margin-top:34px;text-align:left}
.service{display:flex;gap:10px}
.service svg{width:20px;height:20px;flex:none}
.service h4{font-size:9px;font-weight:700;margin-bottom:4px}
.service p{font-size:7px;color:var(--muted);line-height:1.5}

.about{height:320px;background:var(--dark);position:relative}
.about-photo{position:absolute;left:60px;top:60px;width:460px;height:250px;background:linear-gradient(135deg,#5b7fa6,#c9b79a 55,#8f7558);background:linear-gradient(135deg,#5b7fa6 0%,#c9b79a 55%,#8f7558 100%)}
.about-copy{position:absolute;left:560px;top:30px;width:360px;color:#c8ced6}
.about-copy h2{font-size:30px;font-weight:700;color:var(--white);margin:4px 0 14px}
.about-copy p{font-size:8px;line-height:1.6;margin-bottom:8px}
.about-copy .btn{width:90px;background:transparent;border:1px solid var(--blue);color:var(--white);margin-top:8px}

.testimonial{height:460px;position:relative}
.testimonial-copy{position:absolute;left:60px;top:60px;width:430px}
.testimonial-copy p{font-size:9px;color:var(--muted);line-height:1.7}
.testimonial-copy h4{font-size:11px;font-weight:700;margin-top:14px}
.testimonial-copy small{font-size:8px;color:var(--blue)}
.testimonial-photo{position:absolute;left:520px;top:10px;width:400px;height:430px;background:linear-gradient(160deg,#e9ecef 0%,#d2a25a 45%,#8a6a4a 100%)}

.footer{position:absolute;left:0;top:1820px;width:980px;height:500px;background:var(--blue);color:#e5f0fb;display:flex;gap:40px;padding:40px 60px}
.footer .col{width:180px}
.footer h4{font-size:10px;font-weight:700;color:var(--white);margin-bottom:14px}
.footer li{list-style:none;font-size:8px;margin-bottom:10px}
.footer p{font-size:8px;line-height:1.6}
.copyright{position:absolute;left:0;top:2320px;width:980px;height:32px;background:var(--navy);color:#aab4c0;font-size:7px;display:flex;align-items:center;justify-content:space-between;padding:0 60px}
.pay{display:flex;gap:4px}
.pay i{width:18px;height:11px;background:#3a4a60;border-radius:2px}

/* mobile column */
.mobile{position:absolute;left:1004px;top:0;width:192px;height:2352px;background:var(--white);overflow:hidden}
.m-top{height:30px;background:var(--blue-dark);display:flex;align-items:center;justify-content:space-between;padding:0 10px}
.m-top .brand{font-size:8px;color:var(--white)}
.m-top .brand .mark{width:8px;height:8px;background:var(--white)}
.m-burger{width:12px;height:8px;border-top:2px solid #fff;border-bottom:2px solid #fff;position:relative}
.m-hero{height:150px;background:linear-gradient(120deg,#1c1f24,#5a4331);padding:50px 12px;color:#fff}
.m-hero h1{font-size:17px;font-weight:800;line-height:1.1}
.m-hero h1 span{color:var(--blue)}
.m-block{text-align:center;padding:16px 14px}
.m-block svg{width:18px;height:18px}
.m-block h4{font-size:7px;margin:5px 0 3px}
.m-block p{font-size:6px;color:var(--muted);line-height:1.5}
.m-services{background:var(--soft);text-align:center;padding:18px 14px}
.m-services h2{font-size:14px;margin:3px 0 10px}
.m-about{background:var(--dark);padding:18px 14px;color:#c8ced6}
.m-about h2{font-size:14px;color:#fff;margin-bottom:8px}
.m-about p{font-size:6px;line-height:1.5}
.m-photo{height:110px;background:linear-gradient(160deg,#e9ecef,#d2a25a 50%,#8a6a4a)}
.m-footer{background:var(--blue);color:#e5f0fb;padding:16px 14px;height:520px}
.m-footer h4{font-size:7px;color:#fff;margin:10px 0 6px}
.m-footer li{list-style:none;font-size:6px;margin-bottom:5px}
.m-copy{background:var(--navy);height:24px}
</style>
</head>
<body>

<main class="desktop">
  <div class="topbar"><span><i class="dot"></i>+1 555 0142 880</span><span><i class="dot"></i>hello@benchlinehire.test</span></div>
  <header class="header">
    <div class="brand"><span class="mark"></span>BENCHLINE HIRE</div>
    <nav class="nav"><a class="on">HOME</a><a>ABOUT US</a><a>SERVICES</a><a>HIRE US</a><a>GALLERY</a><a>CONTACT US</a></nav>
  </header>

  <section class="hero">
    <div class="hero-photo" role="img" aria-label="Tradesperson working with power tools in a workshop"></div>
    <div class="hero-shade"></div>
    <div class="hero-copy">
      <h1>HIRE TOOLS<br><span>NEXT DOOR</span></h1>
      <p>Lorem Ipsum is simply dummy text of the</p>
    </div>
    <form class="quote-form">
      <div class="field"><i></i>Location</div>
      <div class="field"><i></i>Category</div>
      <div class="field"><i></i>Start date</div>
      <div class="field"><i></i>Duration</div>
      <div class="field"><i></i>2 Days – 1 Week</div>
      <div class="btn">Search</div>
    </form>
  </section>

  <section class="features">
    <div class="feature">
      <svg viewBox="0 0 28 28"><circle cx="14" cy="14" r="12" fill="none" stroke="var(--blue)" stroke-width="2"/><path d="M9 14l4 4 7-8" fill="none" stroke="var(--blue)" stroke-width="2"/></svg>
      <h3>Handpicked Destination</h3>
      <p>Lorem Ipsum is simply dummy text of the printing and typesetting industry. Lorem Ipsum has been the industry's standard dummy.</p>
    </div>
    <div class="feature">
      <svg viewBox="0 0 28 28"><rect x="4" y="7" width="20" height="14" rx="2" fill="none" stroke="var(--blue)" stroke-width="2"/><line x1="4" y1="12" x2="24" y2="12" stroke="var(--blue)" stroke-width="2"/></svg>
      <h3>Best Price Guaranteed</h3>
      <p>Lorem Ipsum is simply dummy text of the printing and typesetting industry. Lorem Ipsum has been the industry's standard dummy.</p>
    </div>
    <div class="feature">
      <svg viewBox="0 0 28 28"><path d="M8 5l4 4-2 3a12 12 0 0 0 6 6l3-2 4 4-3 3C12 23 5 16 5 8z" fill="var(--blue)"/></svg>
      <h3>24/7 Customer Service</h3>
      <p>Lorem Ipsum is simply dummy text of the printing and typesetting industry. Lorem Ipsum has been the industry's standard dummy.</p>
    </div>
  </section>

  <section class="services">
    <div class="eyebrow">Lorem Ipsum is simply dummy text</div>
    <h2>Services</h2>
    <p class="lead">Lorem Ipsum is simply dummy text of the printing and typesetting industry. Lorem Ipsum has been the industry's standard dummy.</p>
    <div class="service-grid">
      <div class="service"><svg viewBox="0 0 20 20"><path d="M3 17l8-8M11 9l3-6 3 3-6 3" stroke="var(--blue)" stroke-width="2" fill="none"/></svg><div><h4>Lorem Ipsum is</h4><p>Lorem Ipsum is simply dummy text of the printing and typesetting.</p></div></div>
      <div class="service"><svg viewBox="0 0 20 20"><rect x="3" y="8" width="14" height="8" fill="var(--blue)"/><rect x="7" y="4" width="6" height="4" fill="none" stroke="var(--blue)" stroke-width="2"/></svg><div><h4>Lorem Ipsum is</h4><p>Lorem Ipsum is simply dummy text of the printing and typesetting.</p></div></div>
      <div class="service"><svg viewBox="0 0 20 20"><circle cx="10" cy="10" r="6" fill="none" stroke="var(--blue)" stroke-width="2"/><circle cx="10" cy="10" r="2" fill="var(--blue)"/></svg><div><h4>Lorem Ipsum is</h4><p>Lorem Ipsum is simply dummy text of the printing and typesetting.</p></div></div>
      <div class="service"><svg viewBox="0 0 20 20"><path d="M4 16L16 4" stroke="var(--blue)" stroke-width="3"/></svg><div><h4>Lorem Ipsum is</h4><p>Lorem Ipsum is simply dummy text of the printing and typesetting.</p></div></div>
      <div class="service"><svg viewBox="0 0 20 20"><rect x="4" y="4" width="12" height="12" fill="none" stroke="var(--blue)" stroke-width="2"/></svg><div><h4>Lorem Ipsum is</h4><p>Lorem Ipsum is simply dummy text of the printing and typesetting.</p></div></div>
      <div class="service"><svg viewBox="0 0 20 20"><path d="M10 3l7 14H3z" fill="var(--blue)"/></svg><div><h4>Lorem Ipsum is</h4><p>Lorem Ipsum is simply dummy text of the printing and typesetting.</p></div></div>
      <div class="service"><svg viewBox="0 0 20 20"><path d="M3 10h14M10 3v14" stroke="var(--blue)" stroke-width="2"/></svg><div><h4>Lorem Ipsum is</h4><p>Lorem Ipsum is simply dummy text of the printing and typesetting.</p></div></div>
      <div class="service"><svg viewBox="0 0 20 20"><circle cx="10" cy="10" r="7" fill="var(--blue)"/></svg><div><h4>Lorem Ipsum is</h4><p>Lorem Ipsum is simply dummy text of the printing and typesetting.</p></div></div>
      <div class="service"><svg viewBox="0 0 20 20"><path d="M4 14l4-8 4 5 4-3" stroke="var(--blue)" stroke-width="2" fill="none"/></svg><div><h4>Lorem Ipsum is</h4><p>Lorem Ipsum is simply dummy text of the printing and typesetting.</p></div></div>
    </div>
  </section>

  <section class="about">
    <div class="about-photo" role="img" aria-label="Worker on a step ladder painting a bright wall"></div>
    <div class="about-copy">
      <div class="eyebrow">What we do</div>
      <h2>About Us</h2>
      <p>Lorem Ipsum is simply dummy text of the printing and typesetting industry. Lorem Ipsum has been the industry's standard dummy text ever since the 1500s, when an unknown printer took a galley of type and scrambled it to make a type specimen book.</p>
      <p>It has survived not only five centuries, but also the leap into electronic typesetting, remaining essentially unchanged. It was popularised in the 1960s with the release of sheets containing passages.</p>
      <div class="btn">Read More</div>
    </div>
  </section>

  <section class="testimonial">
    <div class="testimonial-copy">
      <p>Lorem Ipsum is simply dummy text of the printing and typesetting industry. Lorem Ipsum has been the industry's standard dummy text ever since the 1500s, when an unknown printer took a galley of type and scrambled it to make a type specimen book. It has survived not only five centuries, but also the leap into electronic typesetting, remaining essentially unchanged. It was popularised in the 1960s with the release of Letraset sheets.</p>
      <h4>Martin Hale</h4>
      <small>Company Owner</small>
    </div>
    <div class="testimonial-photo" role="img" aria-label="Builder in hard hat and high-visibility vest holding a drill"></div>
  </section>

  <footer class="footer">
    <div class="col"><h4>Contact Info</h4><p>Lorem Ipsum is simply dummy text of the printing.</p><ul style="margin-top:12px"><li>+1 555 0142 880</li><li>hello@benchlinehire.test</li><li>12 Sample Road</li></ul></div>
    <div class="col"><h4>Destinations</h4><ul><li>Home</li><li>About Us</li><li>Services</li><li>Hire Us</li><li>Gallery</li><li>Contact Us</li></ul></div>
    <div class="col"><h4>Lorem Ipsum is simply</h4><p>Lorem Ipsum is simply dummy text of the printing and typesetting industry. Lorem Ipsum has been the industry's standard dummy text.</p></div>
    <div class="col"><h4>Lorem ipsum</h4><p>Lorem Ipsum is simply dummy text of the printing and typesetting industry. Lorem Ipsum has been the standard.</p></div>
  </footer>
  <div class="copyright"><span>© Copyright 2024 BENCHLINE HIRE. All rights reserved.</span><span class="pay"><i></i><i></i><i></i><i></i></span></div>
</main>

<aside class="mobile">
  <div class="m-top"><div class="brand"><span class="mark"></span>BENCHLINE HIRE</div><div class="m-burger"></div></div>
  <div class="m-hero" role="img" aria-label="Workshop scene with tools"><h1>HIRE TOOLS<br><span>NEXT DOOR</span></h1></div>
  <div class="m-block"><svg viewBox="0 0 28 28"><circle cx="14" cy="14" r="12" fill="none" stroke="var(--blue)" stroke-width="2"/></svg><h4>Handpicked Destination</h4><p>Lorem Ipsum is simply dummy text of the printing.</p></div>
  <div class="m-block"><svg viewBox="0 0 28 28"><rect x="4" y="7" width="20" height="14" fill="none" stroke="var(--blue)" stroke-width="2"/></svg><h4>Best Price Guaranteed</h4><p>Lorem Ipsum is simply dummy text of the printing.</p></div>
  <div class="m-services">
    <div class="eyebrow">Lorem ipsum</div><h2>Services</h2>
    <div class="m-block"><svg viewBox="0 0 20 20"><circle cx="10" cy="10" r="6" fill="var(--blue)"/></svg><h4>Lorem Ipsum is</h4><p>Lorem Ipsum is simply dummy text.</p></div>
    <div class="m-block"><svg viewBox="0 0 20 20"><rect x="4" y="4" width="12" height="12" fill="var(--blue)"/></svg><h4>Lorem Ipsum is</h4><p>Lorem Ipsum is simply dummy text.</p></div>
    <div class="m-block"><svg viewBox="0 0 20 20"><path d="M10 3l7 14H3z" fill="var(--blue)"/></svg><h4>Lorem Ipsum is</h4><p>Lorem Ipsum is simply dummy text.</p></div>
    <div class="m-block"><svg viewBox="0 0 20 20"><path d="M4 16L16 4" stroke="var(--blue)" stroke-width="3"/></svg><h4>Lorem Ipsum is</h4><p>Lorem Ipsum is simply dummy text.</p></div>
  </div>
  <div class="m-about"><div class="eyebrow">What we do</div><h2>About Us</h2><p>Lorem Ipsum is simply dummy text of the printing and typesetting industry. Lorem Ipsum has been the industry's standard dummy text ever since.</p></div>
  <div class="m-block" style="text-align:left"><p>Lorem Ipsum is simply dummy text of the printing and typesetting industry.</p><h4>Martin Hale</h4></div>
  <div class="m-photo" role="img" aria-label="Builder holding a drill"></div>
  <div class="m-footer">
    <h4>Contact Info</h4><ul><li>+1 555 0142 880</li><li>hello@benchlinehire.test</li></ul>
    <h4>Destinations</h4><ul><li>Home</li><li>About Us</li><li>Services</li><li>Hire Us</li><li>Gallery</li><li>Contact Us</li></ul>
    <h4>Lorem Ipsum is simply</h4><ul><li>Lorem Ipsum is simply dummy text.</li></ul>
  </div>
  <div class="m-copy"></div>
</aside>

</body>
</html>
```